Modern Label for Loose Tea pouches on 4.5x6 Label

We need a new label for our teas that is very simple in design, but stylish and modern. This will be used to print labels for our loose tea pouches. The label will be at max 4.5x6 inches in size. There should be a place for the tea name, description, ingredients, and size that is changeable.
Preferably an AI file that allows me to setup variables to change the above items. There will also need to be our logo which is supplied, and our address on the label.
Address:
Brevo Leaf
846 Lower Maple Lane
Highland, NY 12617
Target Market(s)
Tea Lovers
Requirements
Must have
- Adobe Illustrator file with variables setup for replacement of tea name, description, ingredients, and size (weights 2oz, 4oz, 8oz, 1lb)

```html
<!DOCTYPE html>
<html lang="en">
<head>
<meta charset="utf-8">
<title>Acai Berry White – Tea Label</title>
<link rel="stylesheet" href="https://fonts.googleapis.com/css2?family=Bebas+Neue&family=Open+Sans:wght@400;600;700&family=Oswald:wght@300;500&display=swap">
<style>
  :root {
    --lime: #c2e012;
    --lime-text: #8cc63f;
    --pink: #e6318f;
    --ink: #1c1c1c;
    --rule: #3a3a3a;
    --paper: #ffffff;
    --stage: #f2f2f2;
  }
  * { box-sizing: border-box; margin: 0; padding: 0; }
  html, body { width: 1200px; height: 800px; overflow: hidden; background: var(--stage); }
  .canvas { position: relative; width: 1200px; height: 800px; }
  .label {
    position: absolute; left: 315px; top: 20px;
    width: 570px; height: 760px; overflow: hidden;
    background: var(--lime);
    font-family: "Open Sans", Arial, sans-serif; color: var(--ink);
  }
  .label-frame { position: absolute; inset: 0; }
  .brand {
    position: absolute; top: 196px; left: 0; width: 100%;
    display: flex; justify-content: center; align-items: center; gap: 10px;
  }
  .brand-mark { width: 14px; height: 14px; border-radius: 50%; background: var(--pink); }
  .brand-name { font-weight: 700; font-size: 26px; letter-spacing: 2px; color: var(--pink); }
  .rule {
    position: absolute; left: 83px; width: 418px; height: 17px;
    border-top: 5px solid var(--rule); border-bottom: 5px solid var(--rule);
    background: repeating-linear-gradient(90deg, var(--rule) 0 1px, transparent 1px 3px);
  }
  .rule-top { top: 231px; }
  .rule-bottom { top: 325px; }
  .tea-name {
    position: absolute; top: 256px; left: 0; width: 100%;
    text-align: center; font-family: "Bebas Neue", "Oswald", sans-serif;
    font-size: 60px; line-height: 64px; color: var(--ink);
  }
  .leaf { position: absolute; top: 268px; width: 34px; height: 36px; }
  .leaf-left { left: 84px; }
  .leaf-right { left: 466px; }
  .description {
    position: absolute; top: 355px; left: 80px; width: 430px;
    font-size: 17.4px; line-height: 23.5px;
  }
  .ingredients {
    position: absolute; top: 470px; left: 77px; width: 440px;
    font-size: 15.6px; line-height: 21px;
  }
  .ingredients-title { font-weight: 700; color: var(--lime-text); font-size: 17px; }
  .net-weight {
    position: absolute; top: 540px; left: 98px; width: 100px; text-align: center;
  }
  .net-weight-label { font-family: "Oswald", sans-serif; font-weight: 300; font-size: 22px; line-height: 26px; }
  .net-weight-value { font-weight: 700; font-size: 18px; color: var(--lime-text); margin-top: 6px; }
  .address {
    position: absolute; top: 540px; left: 205px; padding-left: 8px; height: 78px;
    border-left: 2px solid var(--ink);
    font-size: 13.3px; line-height: 18px;
  }
  .address-title { font-family: "Oswald", sans-serif; font-weight: 500; font-size: 15px; margin-bottom: 8px; }
  .brand-badge {
    position: absolute; top: 545px; left: 367px; width: 110px; height: 110px;
    border-radius: 50%; background: var(--pink); opacity: .9;
  }
</style>
</head>
<body>
<main class="canvas">
  <section class="label">
    <svg class="label-frame" width="570" height="760" viewBox="0 0 570 760" aria-hidden="true">
      <ellipse cx="290" cy="372" rx="282" ry="318" fill="var(--paper)"/>
    </svg>

    <div class="brand">
      <span class="brand-mark"></span>
      <span class="brand-name">BREVO LEAF</span>
    </div>

    <div class="rule rule-top"></div>
    <svg class="leaf leaf-left" viewBox="0 0 34 36" role="img" aria-label="Leaf ornament">
      <ellipse cx="17" cy="18" rx="15" ry="16" fill="var(--lime-text)"/>
    </svg>
    <h1 class="tea-name">Acai Berry White</h1>
    <svg class="leaf leaf-right" viewBox="0 0 34 36" role="img" aria-label="Leaf ornament">
      <ellipse cx="17" cy="18" rx="15" ry="16" fill="var(--lime-text)"/>
    </svg>
    <div class="rule rule-bottom"></div>

    <p class="description">Delicious and good for you. This loose leaf white tea blend features “super food” acai mixed delicately with exotic, flavorful berries to create a deliciously flavorful white tea blend packed with antioxidants.</p>

    <p class="ingredients"><span class="ingredients-title">INGREDIENTS:</span>White tea scented with natural Acai berry and sprinkled with blue corn flowers.</p>

    <div class="net-weight">
      <div class="net-weight-label">NET WEIGHT</div>
      <div class="net-weight-value">1lb(454g)</div>
    </div>

    <address class="address" style="font-style:normal">
      <div class="address-title">ADDRESS:</div>
      Brevo Leaf<br>846 Lower Maple Lane<br>Highland, NY 12617
    </address>

    <div class="brand-badge"></div>
  </section>
</main>
</body>
</html>
```